MAXI Fest am Lindenbühl - big party night in Straubing

For a party in the Konrad-Weidinger Halle in Straubing, an attractive poster for "party people" is to be created. The poster should attract at least 3000 visitors. The poster (DIN A 2) will be rebuilt by us for further use as an A5 Flyer and should thus ensure the recognition. There are no special conditions regarding colors and design - but the texts mentioned in the annex must be included. The attached photos can be used in any number and / or in excerpts (we will then insert the original high-resolution files ourselves) Important is the communication: Party Where When A reference to the KVMB as organizer is not welcome (except in the imprint) , Although the party takes place in the context of the KVMB Tri-town tour, the poster should primarily address the general party people. The fans around the rally are coming anyway. Pixel Forge - Description Date: 7th May 2018 Title: MAXI Fest am Lindenbühl am 20. October 2018 possible title signature (optional, also changeable) Halle der Helden! or The hall shakes! or hall tremors with 3,000 party people or hall opening at 7 pm - open end Konrad-Weidinger Halle in Straubing Content (all 5 lines compulsory) • Cult band Gustl and the chrome bumpers • Prairie Town with DJ Rodeo shooting booths • Salon Fortuna with roulette Table • Cult figure Kurvnrutscher • Large season-closing party for the KVMB Dreiländer-Tour Website www.dreilaender-tour-ost.de Imprint: Organizer: KVMB Oberpfalz eV, Kestnerweg 12, 80917 Munich E-Mail: motor@opf.kvmb-verein.de, Tel. : 089 - 7462 308 --------------------------------------------- ------------------------------------------ Colors: Free Format: DIN A2 logos : no font: if it is not a design element we prefer Calibri - but remains free to the designer Additional semicolons to the event (for information only): Saturday: The mega-rally party in the Weidinger-Halle From 18 o'clock hall opening - Our Acts : - Gustl and the chrome bumpers (from 20: 30/21 clock) - Prairie Town in Foyer 2 (award ceremony KVMB eV); then open to all with Rodeo etc. (Markus is checking cooperation with Dakota Ranch) and own DJ - show involvement of Verena as a "good mood" host, especially in the time between 6pm and 9pm: Interviews, Acts or Trials the Western-Arena or the casino etc. - The "small" Auwiesenmarkt with dice, Hau the Luke etc.

Colors

Designer to choose colors to be used in the design.

Requirements

```html
<!DOCTYPE html>
<html lang="de">
<head>
<meta charset="utf-8">
<title>MAXI Fest am Lindenbühl</title>
<link href="https://fonts.googleapis.com/css2?family=Alfa+Slab+One&family=Figtree:wght@400;500&display=swap" rel="stylesheet">
<style>
  :root {
    --backdrop: #d9d6d1;
    --paper: #f2f1ee;
    --ink: #1f1f1f;
  }
  html, body {
    margin: 0;
    width: 937px;
    height: 1200px;
    overflow: hidden;
    background: var(--backdrop);
  }
  .poster {
    position: absolute;
    left: 58px;
    top: 20px;
    width: 820px;
    height: 1160px;
    background: var(--paper);
    color: var(--ink);
    font-family: "Figtree", sans-serif;
    overflow: hidden;
  }
  .headline {
    position: absolute;
    inset: 0;
    width: 820px;
    height: 1160px;
  }
  .headline text {
    font-family: "Alfa Slab One", serif;
    fill: var(--ink);
  }
  .info {
    position: absolute;
    margin: 0;
    font-size: 16px;
    line-height: 1.3;
    font-weight: 400;
  }
  .info--opening { left: 41px; top: 36px; }
  .info--venue { left: 41px; top: 80px; }
  .event-date {
    position: absolute;
    left: 91px;
    top: 218px;
    margin: 0;
    font-size: 28px;
    font-weight: 400;
  }
  .programme {
    position: absolute;
    left: 41px;
    top: 1024px;
    margin: 0;
    padding: 0;
    list-style: none;
    font-size: 17px;
    line-height: 1.36;
  }
  .imprint {
    position: absolute;
    left: 604px;
    top: 1020px;
    font-size: 11.5px;
    line-height: 1.4;
  }
  .imprint p { margin: 0; }
  .imprint .website { margin-bottom: 22px; }
</style>
</head>
<body>
<main class="poster">
  <svg class="headline" viewBox="0 0 820 1160" aria-label="MAXI Fest am Lindenbühl">
    <text class="headline__word" font-size="292" transform="translate(245 949) rotate(-90)" textLength="640" lengthAdjust="spacingAndGlyphs">MAXI</text>
    <text class="headline__word" font-size="300" transform="translate(631 949) rotate(-90)" textLength="916" lengthAdjust="spacingAndGlyphs">FEST</text>
    <text class="headline__word" font-size="158" transform="translate(784 949) rotate(-90)" textLength="916" lengthAdjust="spacingAndGlyphs">AM LINDENBÜHL</text>
  </svg>

  <p class="info info--opening">Hallenöffnung um 19 Uhr</p>
  <p class="info info--venue">Konrad-Weidinger Halle<br>in Straubing</p>
  <p class="event-date">20. Oktober 2018</p>

  <ul class="programme">
    <li>Kult-Band Gustl und die Chromstoßstangen</li>
    <li>Prairie-Town mit DJ + Rodeo + Wurfbuden</li>
    <li>Salon Fortuna mit Roulette-Tisch</li>
    <li>Kult-Figur Kurvnrutscher</li>
    <li>Große Saison-Abschlussparty zur KVMB Dreiländer-Tour</li>
  </ul>

  <div class="imprint">
    <p class="website">www.dreilaender-tour-ost.de</p>
    <p>Veranstalter:</p>
    <p>KVMB Oberpfalz e.V.,</p>
    <p>Kestnerweg 12, 80917 München</p>
    <p>E-Mail: motor@opf.kvmb-verein.de</p>
    <p>Tel.: 089 – 7462 308</p>
  </div>
</main>
</body>
</html>
```